Simple and clean webdesign for personal homepage

Trying to create a simple and clean webdesign for my personal homepage. Going to use a static site builder with templates to build the site. I want it to have multiple pages - like an about me, blog and resume. I just need something very basic I can customize. I want the main colors to be purple, black and white. I am open to other color palettes too but since purple is my favorite color I want that to be one of the main colors.

The site be mostly text driven. Might have some images in the body text but I want the site design to be light and lean.

Industry/Entity Type

Personal Homepage.

Coding

Coded - Design and coding required

Number of Pages Required

1 page

Font styles to use
Sans Serif

Colors
6B429C
8869AF
B7A5CE
E3DAEB
F3F0F8

Requirements
Must have
• Clean design. Purple used as a color. HTML template.
Nice to have
• Responsive

```html
<!DOCTYPE html>
<html lang="en">
<head>
<meta charset="UTF-8">
<title>Personal Blog</title>
<link href="https://fonts.googleapis.com/css2?family=Poppins:wght@300;400;500;600;700;800&display=swap" rel="stylesheet">
<style>
:root{
  --purple:#8a10d8;
  --purple-dark:#6B429C;
  --purple-mid:#8869AF;
  --lilac:#B7A5CE;
  --lavender:#E3DAEB;
  --mist:#F3F0F8;
  --ink:#111111;
  --text:#555555;
  --muted:#8a8a8a;
  --white:#ffffff;
}
*{margin:0;padding:0;box-sizing:border-box}
html,body{width:1200px;height:5192px;overflow:hidden}
body{font-family:'Poppins',sans-serif;background:var(--white);color:var(--ink);position:relative}
.abs{position:absolute}
.section-title{position:absolute;left:0;width:1200px;text-align:center;font-size:38px;font-weight:600;color:var(--ink)}
.section-sub{position:absolute;left:0;width:1200px;text-align:center;font-size:13px;color:var(--text)}
.pill-btn{position:absolute;background:var(--purple);color:var(--white);border-radius:40px;font-size:14px;font-weight:500;display:flex;align-items:center;justify-content:center;text-transform:uppercase}
.photo{position:absolute;overflow:hidden}

/* header */
.logo{left:60px;top:30px;font-size:30px;font-weight:600;letter-spacing:.5px}
.nav{right:230px;top:40px;display:flex;gap:22px;font-size:13px;font-weight:500;text-transform:uppercase}
.hero-circle{left:720px;top:-180px;width:540px;height:540px;border-radius:50%;background:radial-gradient(circle at 40% 40%,#e6c9f7,#d4a8f0)}
.hero-circle-b{left:820px;top:-200px;width:460px;height:460px;border-radius:50%;background:#dcb6f5;opacity:.6}
.hero-photo{left:600px;top:120px;width:480px;height:560px;border-radius:100px 100px 0 0;background:linear-gradient(160deg,#f4f4f4,#e6e6e6 60%,#d9d9d9)}
.scroll-label{left:1120px;top:470px;font-size:10px;color:var(--muted);transform:rotate(90deg);letter-spacing:1px}
.welcome{left:60px;top:240px;font-size:14px;font-weight:500;color:var(--purple);text-transform:uppercase}
.hello{left:60px;top:262px;font-size:66px;font-weight:800;line-height:1}
.client{left:60px;top:328px;font-size:66px;font-weight:800;color:var(--purple);line-height:1.05;text-transform:uppercase}
.role{left:60px;top:416px;font-size:22px;font-weight:600}
.role span{color:var(--purple);font-weight:500}
.hero-text{left:60px;top:462px;width:420px;font-size:12px;color:var(--text);line-height:1.6}
.follow{left:60px;top:664px;display:flex;align-items:center;gap:12px;font-size:12px;color:var(--muted)}
.follow .dot{width:34px;height:34px;border:1.5px solid var(--purple);border-radius:50%}

/* feature */
.feature-panel{left:232px;top:1120px;width:728px;height:180px;background:var(--mist)}
.card{position:absolute;top:872px;width:268px;height:308px;overflow:hidden}
.card .tag{position:absolute;left:14px;bottom:96px;background:var(--purple);color:var(--white);font-size:10px;padding:4px 12px;border-radius:3px}
.card .cap{position:absolute;left:14px;right:14px;bottom:40px;color:var(--white);font-size:13px;font-weight:500;line-height:1.35}
.dots{left:520px;top:1218px;display:flex;gap:12px;align-items:center}
.dots span{width:10px;height:10px;border-radius:50%;border:1.5px solid var(--lilac)}
.dots span.on{background:var(--purple);border-color:var(--purple)}

/* about */
.about-card{left:152px;top:1500px;width:896px;height:480px;border-radius:30px;background:linear-gradient(180deg,#f7effc,#efddfb)}
.about-circle{left:880px;top:1450px;width:380px;height:380px;border-radius:50%;background:#e9d2f8}
.about-photo{left:690px;top:1540px;width:330px;height:400px;border-radius:24px;background:linear-gradient(150deg,#8d9c5e,#5f6f38);opacity:.85}
.about-name{left:204px;top:1560px;font-size:32px;font-weight:600}
.about-role{left:204px;top:1608px;font-size:15px}
.about-role span{color:var(--purple)}
.about-text{left:204px;top:1640px;width:440px;font-size:11px;color:var(--text);line-height:1.6}
.info{left:204px;top:1720px;display:grid;grid-template-columns:80px 118px 80px 170px;row-gap:10px;font-size:11px;color:var(--text)}
.info b{font-weight:500;color:var(--ink)}
.cv-btn{left:204px;top:1852px;width:164px;height:44px;font-size:12px}

/* resume */
.col-title{top:2056px;font-size:18px;font-weight:600}
.col-box{top:2090px;height:450px;border:1px solid #ececec;border-radius:4px;box-shadow:0 6px 18px rgba(0,0,0,.05)}
.exp-box{background:linear-gradient(180deg,#efe2fa,#f6effc)}
.entry{position:absolute;left:24px;width:270px}
.entry .year{display:inline-block;font-size:10px;padding:3px 14px;border-radius:20px;background:var(--purple);color:var(--white);margin-bottom:8px}
.entry .year.line{background:transparent;color:var(--purple);border:1px solid var(--purple)}
.entry h4{font-size:15px;font-weight:500}
.entry h4.accent{color:var(--purple)}
.entry p{font-size:10px;color:var(--text);line-height:1.5}
.skill{position:absolute;left:804px;width:296px}
.skill .label{font-size:11px;font-weight:500}
.skill .bar{margin-top:6px;height:6px;background:#222;position:relative}
.skill .fill{position:absolute;left:0;top:0;height:6px;background:var(--purple)}
.skill .pct{position:absolute;top:-30px;font-size:10px;background:var(--white);border:1px solid #333;padding:2px 8px}

/* projects */
.projects-band{left:0;top:2600px;width:940px;height:840px;background:var(--mist)}
.proj{position:absolute;width:280px;height:270px;border-radius:10px}
.proj-label{position:absolute;left:172px;top:3010px;color:var(--purple);font-size:15px;font-weight:500}

/* blog */
.post-img{position:absolute;left:176px;width:264px;height:210px}
.post-date{position:absolute;left:392px;width:72px;height:30px;background:var(--purple);color:var(--white);font-size:11px;display:flex;align-items:center;justify-content:center}
.post{position:absolute;left:492px;width:560px}
.post h3{font-size:17px;font-weight:600;line-height:1.35}
.post p{margin-top:12px;font-size:11px;color:var(--text);line-height:1.65}
.post .more{margin-top:18px;font-size:12px;color:var(--purple);display:flex;align-items:center;gap:10px}
.explore{left:0;width:1200px;top:4360px;text-align:center;font-size:12px;color:var(--purple)}

/* newsletter */
.news-band{left:280px;top:4460px;width:920px;height:280px;border-radius:140px 0 0 140px;background:linear-gradient(90deg,#f3e6fc,#d7aef3)}
.news-ring{left:72px;top:4444px;width:360px;height:360px;border-radius:50%;background:#c98ff0}
.news-photo{left:92px;top:4464px;width:320px;height:320px;border-radius:50%;background:radial-gradient(circle at 50% 50%,#eef0e4,#7d9657 70%,#5e7a3b)}
.news-title{left:484px;top:4508px;font-size:32px;font-weight:600}
.news-sub{left:484px;top:4560px;font-size:11px;color:var(--text)}
.news-input{left:484px;top:4606px;width:388px;height:42px;background:var(--white);border-radius:22px 0 0 22px;font-size:11px;color:var(--muted);padding:13px 22px}
.news-btn{left:866px;top:4606px;width:140px;height:42px;font-size:12px}

/* footer */
.foot-logo{left:72px;top:4962px;font-size:26px;font-weight:600}
.foot-social{left:130px;top:5010px;display:flex;gap:8px}
.foot-social span{width:32px;height:32px;border-radius:50%;background:var(--purple)}
.foot-head{top:4806px;font-size:15px;font-weight:600;text-transform:uppercase}
.foot-list{top:4848px;font-size:11px;color:var(--text);line-height:2}
.contact-row{display:flex;align-items:flex-start;gap:8px;font-size:11px;color:var(--text);margin-bottom:14px}
.contact-row svg{flex:none;margin-top:2px}
.latest{display:flex;gap:10px;margin-bottom:18px}
.latest .thumb{width:46px;height:46px;border-radius:50%;background:linear-gradient(135deg,#c9a88a,#7c5a45);flex:none}
.latest small{font-size:10px;color:var(--purple);display:block}
.latest p{font-size:10px;color:var(--text);line-height:1.4}
.copyright{left:0;width:1200px;top:5150px;text-align:center;font-size:10px;color:var(--muted)}
</style>
</head>
<body>

<!-- Header -->
<div class="abs hero-circle"></div>
<div class="abs hero-circle-b"></div>
<div class="abs logo">PERSONAL BLOG</div>
<nav class="abs nav"><span>Home</span><span>About Me</span><span>Reviews</span><span>Projects</span><span>Blog</span></nav>
<div class="pill-btn" style="left:996px;top:28px;width:144px;height:42px">Contact Us</div>

<!-- Hero -->
<div class="photo hero-photo" role="img" aria-label="Bright room corner with a wall clock, desk lamp and potted plant"></div>
<div class="abs scroll-label">SCROLL DOWN</div>
<div class="abs welcome">Welcome to my world</div>
<div class="abs hello">HELLO I,M</div>
<div class="abs client">Client Name</div>
<div class="abs role">A Professional <span>Blogger.</span></div>
<p class="abs hero-text">Lorem ipsum has been the industry's standard dummy text ever since the 1500s, when an unknown printer took a galley of type and scrambled it to make a type book.</p>
<div class="abs follow">Follow Us On <span class="dot"></span><span class="dot"></span><span class="dot"></span></div>

<!-- Feature Blog -->
<div class="section-title" style="top:776px">Feature Blog</div>
<div class="abs feature-panel"></div>
<div class="card" style="left:-108px" role="img" aria-label="Blog cover photo of a desk setup"><div class="photo" style="inset:0;background:linear-gradient(180deg,#7a5c44,#3b2b20)"></div><div class="cap">has been the industry's standard text ever since</div></div>
<div class="card" style="left:172px"><div class="photo" style="inset:0;background:linear-gradient(180deg,#b59a7e,#4a3a2e)" role="img" aria-label="Blog cover photo of a person writing"></div><span class="tag">Health Life</span><div class="cap">Lorem Ipsum has been the industry's standard text ever since the when</div></div>
<div class="card" style="left:460px"><div class="photo" style="inset:0;background:linear-gradient(180deg,#d9cfc3,#5a4b40)" role="img" aria-label="Blog cover photo of friends laughing"></div><span class="tag">Travel</span><div class="cap">Lorem Ipsum has been the industry's standard text ever since the from</div></div>
<div class="card" style="left:752px"><div class="photo" style="inset:0;background:linear-gradient(180deg,#cfd4d8,#4b5056)" role="img" aria-label="Blog cover photo of a man relaxing at his desk"></div><span class="tag">Professional</span><div class="cap">Lorem Ipsum has been the industry's standard text ever since the</div></div>
<div class="card" style="left:1048px"><div class="photo" style="inset:0;background:linear-gradient(180deg,#e4e4e4,#6b6b6b)" role="img" aria-label="Blog cover photo of a person working"></div><span class="tag">Business</span><div class="cap">Lorem Ipsum has been the industry's text</div></div>
<div class="abs dots"><span></span><span></span><span class="on"></span><span></span><span></span></div>

<!-- About -->
<div class="section-title" style="top:1380px">About Me</div>
<div class="section-sub" style="top:1446px">Lorem Ipsum has been the industry's standard dummy text ever since the 1</div>
<div class="abs about-card"></div>
<div class="abs about-circle"></div>
<div class="photo about-photo" role="img" aria-label="Photo of a large green leaf"></div>
<div class="abs about-name">Client Name</div>
<div class="abs about-role">A Lead <span>Professional</span> Based in Area Name</div>
<p class="abs about-text">Lorem ipsum has been the industry's standard dummy text ever since the 1500s, when an unknown printer took a galley of type and scrambled it to make a type specimen book it has survived not only five centuries.</p>
<div class="abs info">
  <span>Name:</span><b>Blogger Name</b><span>DOB:</span><b>00 - Month 0000</b>
  <span>Age:</span><b>00 Year</b><span>Phone:</span><b>+00 000 000 0000</b>
  <span>Nationality:</span><b>Country</b><span>Email:</span><b>hello@example.com</b>
  <span>Freelance:</span><b>Available</b><span>Languages:</span><b>French, English</b>
</div>
<div class="pill-btn cv-btn">Download CV</div>

<!-- Resume -->
<div class="abs col-title" style="left:80px">Education</div>
<div class="abs col-title" style="left:432px">Experience</div>
<div class="abs col-title" style="left:784px">My Skills</div>
<div class="abs col-box" style="left:80px;width:320px"></div>
<div class="abs col-box exp-box" style="left:432px;width:328px"></div>
<div class="abs col-box" style="left:784px;width:336px"></div>

<div class="entry" style="left:104px;top:2160px"><span class="year">2020 - 2024</span><h4>Computer Science -</h4><p>Lorem Ipsum has been the industry's standard</p></div>
<div class="entry" style="left:104px;top:2276px"><span class="year line">2020 - 2024</span><h4>Computer Science -</h4><p>Lorem Ipsum has been the industry's standard</p></div>
<div class="entry" style="left:104px;top:2392px"><span class="year">2020 - 2024</span><h4>Computer Science -</h4><p>Lorem Ipsum has been the industry's standard</p></div>

<div class="entry" style="left:456px;top:2160px"><span class="year line">2020 - 2024</span><h4 class="accent">Software Company</h4><p>Lorem Ipsum has been the industry's standard</p></div>
<div class="entry" style="left:456px;top:2276px"><span class="year line">2020 - 2024</span><h4 class="accent">Digital marketing</h4><p>Lorem Ipsum has been the industry's standard</p></div>
<div class="entry" style="left:456px;top:2392px"><span class="year line">2020 - 2024</span><h4 class="accent">SEO</h4><p>Lorem Ipsum has been the industry's standard</p></div>

<div class="skill" style="top:2168px"><div class="label">Skill Name</div><div class="bar"><div class="fill" style="width:80%"></div><span class="pct" style="left:72%">80%</span></div></div>
<div class="skill" style="top:2236px"><div class="label">Skill Name</div><div class="bar"><div class="fill" style="width:65%"></div><span class="pct" style="left:57%">70%</span></div></div>
<div class="skill" style="top:2304px"><div class="label">Skill Name</div><div class="bar"><div class="fill" style="width:85%"></div><span class="pct" style="left:78%">90%</span></div></div>
<div class="skill" style="top:2372px"><div class="label">Skill Name</div><div class="bar"><div class="fill" style="width:70%"></div><span class="pct" style="left:62%">60%</span></div></div>
<div class="skill" style="top:2440px"><div class="label">Skill Name</div><div class="bar"><div class="fill" style="width:80%"></div><span class="pct" style="left:72%">80%</span></div></div>

<!-- Projects -->
<div class="abs projects-band"></div>
<div class="section-title" style="top:2676px">Our Projects</div>
<div class="section-sub" style="top:2738px">Lorem Ipsum has been the industry's standard dummy text ever since the 1</div>
<div class="proj" style="left:152px;top:2788px;background:linear-gradient(135deg,#3a2a44,#1a1420)" role="img" aria-label="Project: dark branding mockup"></div>
<div class="proj-label">Project Name</div>
<div class="proj" style="left:460px;top:2788px;background:linear-gradient(135deg,#a0664a,#2f5b4e)" role="img" aria-label="Project: stationery mockup on green and orange"></div>
<div class="proj" style="left:768px;top:2788px;background:linear-gradient(135deg,#2b2b2b,#4a4a4a)" role="img" aria-label="Project: dark desk workspace"></div>
<div class="proj" style="left:152px;top:3092px;background:linear-gradient(90deg,#bfbfbf,#eeeeee 50%,#1c1c1c 50%)" role="img" aria-label="Project: business card mockup"></div>
<div class="proj" style="left:460px;top:3092px;background:linear-gradient(135deg,#f2d640,#e25c7a 50%,#3bb3d9)" role="img" aria-label="Project: colourful pattern print"></div>
<div class="proj" style="left:768px;top:3092px;background:linear-gradient(135deg,#9fd8c0,#e9f4ef)" role="img" aria-label="Project: responsive website screens"></div>

<!-- Blog -->
<div class="section-title" style="top:3530px">BLOG POST</div>

<div class="post-img" style="top:3620px;background:linear-gradient(160deg,#b7c7cf,#5c6a62)" role="img" aria-label="Blog photo: person walking outdoors"></div>
<div class="post-date" style="top:3614px">00 Jan</div>
<div class="post" style="top:3624px"><h3>Lorem Ipsum Is Simply Dummy Text Of The Printing And Typesetting Industry.</h3><p>Lorem ipsum has been the industry's standard dummy text ever since the 1500s, when an unknown printer took a galley of type and scrambled it to make a type specimen book it has survived not only five centuries.</p><div class="more">Read More <svg width="28" height="8" viewBox="0 0 28 8"><path d="M0 4h26M22 1l4 3-4 3" stroke="#8a10d8" fill="none" stroke-width="1.3"/></svg></div></div>

<div class="post-img" style="top:3872px;background:linear-gradient(160deg,#6b4a3c,#2a1e1b)" role="img" aria-label="Blog photo: creator with a ring light"></div>
<div class="post-date" style="top:3866px">00 Jan</div>
<div class="post" style="top:3876px"><h3>Lorem Ipsum Is Simply Dummy Text Of The Printing And Typesetting Industry.</h3><p>Lorem ipsum has been the industry's standard dummy text ever since the 1500s, when an unknown printer took a galley of type and scrambled it to make a type specimen book it has survived not only five centuries.</p><div class="more">Read More <svg width="28" height="8" viewBox="0 0 28 8"><path d="M0 4h26M22 1l4 3-4 3" stroke="#8a10d8" fill="none" stroke-width="1.3"/></svg></div></div>

<div class="post-img" style="top:4128px;background:linear-gradient(160deg,#d8a56c,#6d4a33)" role="img" aria-label="Blog photo: person working at a laptop"></div>
<div class="post-date" style="top:4122px">00 Jan</div>
<div class="post" style="top:4132px"><h3>Lorem Ipsum Is Simply Dummy Text Of The Printing And Typesetting Industry.</h3><p>Lorem ipsum has been the industry's standard dummy text ever since the 1500s, when an unknown printer took a galley of type and scrambled it to make a type specimen book it has survived not only five centuries.</p><div class="more">Read More <svg width="28" height="8" viewBox="0 0 28 8"><path d="M0 4h26M22 1l4 3-4 3" stroke="#8a10d8" fill="none" stroke-width="1.3"/></svg></div></div>

<div class="abs explore">Explore More</div>

<!-- Newsletter -->
<div class="abs news-band"></div>
<div class="abs news-ring"></div>
<div class="photo news-photo" role="img" aria-label="Top view of a coffee cup, notebook and green leaves"></div>
<div class="abs news-title">Saty Upto Date With Us !</div>
<div class="abs news-sub">Would you like to receive our exclusive updates for Subscriber Today!</div>
<div class="abs news-input">Enter Email *</div>
<div class="pill-btn news-btn">Subscribe</div>

<!-- Footer -->
<div class="abs foot-logo">PERSONAL BLOG</div>
<div class="abs foot-social"><span></span><span></span><span></span></div>

<div class="abs foot-head" style="left:336px">Sitemap</div>
<div class="abs foot-list" style="left:336px">Home<br>About Us<br>Reviews<br>Projects<br>Blog<br>Contact Us</div>

<div class="abs foot-head" style="left:612px">Contact Us</div>
<div class="abs" style="left:612px;top:4850px;width:230px">
  <div class="contact-row"><svg width="12" height="12" viewBox="0 0 12 12"><path d="M2 1l2 0 1 3-1.5 1a6 6 0 0 0 3.5 3.5L8 7l3 1v2a1 1 0 0 1-1 1A9 9 0 0 1 1 2a1 1 0 0 1 1-1z" fill="#8a10d8"/></svg>+00 000 000 0000</div>
  <div class="contact-row"><svg width="12" height="12" viewBox="0 0 12 12"><rect x="1" y="2.5" width="10" height="7" rx="1" fill="none" stroke="#8a10d8"/><path d="M1 3l5 4 5-4" stroke="#8a10d8" fill="none"/></svg>hello@example.com</div>
  <div class="contact-row"><svg width="12" height="12" viewBox="0 0 12 12"><path d="M6 11S2 7 2 4.5a4 4 0 0 1 8 0C10 7 6 11 6 11z" fill="#8a10d8"/><circle cx="6" cy="4.5" r="1.4" fill="#fff"/></svg>Lorem ipsum simply dummy text<br>of the typesetting industry.</div>
</div>

<div class="abs foot-head" style="left:888px">Latest Blog</div>
<div class="abs" style="left:888px;top:4850px;width:240px">
  <div class="latest"><div class="thumb" role="img" aria-label="Blog thumbnail"></div><div><small>00 January 2024</small><p>Lorem ipsum simple text and print typesetting industry.</p></div></div>
  <div class="latest"><div class="thumb" role="img" aria-label="Blog thumbnail"></div><div><small>00 January 2024</small><p>Lorem ipsum simple text and print typesetting industry.</p></div></div>
</div>

<div class="abs copyright">PERSONAL BLOG · 2024 All rights reserved</div>

</body>
</html>
```